Taking a stock layout (purchased) and making it consistent with our brand standards

Designers,

A friend of mine for a Catholic school district needs help with a poster.

The district consists of one high school and one elementary school. The poster design should be compatible for both schools. The schools have separate logos, but similar colors, so the poster designs should simply work for both (logos interchangeable, one logo on the design - NOT both).

My friend liked the following stock layout: http://www.plumfernprints.net/Files/PDF/Range/QM418-Range.pdf , so I purchased the attached native files.

So my project is to simply take the designs from the native files, and make a poster compatible with our brand colors/logo. I've attached PDFs of our current brochures (to use for colors) and the logos for both schools.

Reason: Have 2 great options, but I'm paying 3 spots so I'd like to get some more options

School

```html
<!DOCTYPE html>
<html lang="en">
<head>
<meta charset="utf-8">
<title>Education Is the Foundation – Poster</title>
<link rel="stylesheet" href="https://fonts.googleapis.com/css2?family=Montserrat:wght@700&family=Arimo:wght@700&family=Tinos&display=swap">
<style>
  :root {
    --navy: #1b4f84;
    --blue-deep: #12406e;
    --blue-mid: #1467b3;
    --blue-bright: #2e8fce;
    --blue-light: #76b9e4;
    --orange: #f7a83e;
    --body-grey: #555a5f;
    --white: #ffffff;
  }
  * { margin: 0; padding: 0; box-sizing: border-box; }
  html, body { width: 867px; height: 1200px; overflow: hidden; background: var(--white); }
  .poster { position: relative; width: 867px; height: 1200px; }
  .panel { position: absolute; left: 0; width: 867px; height: 600px; }
  .panel--top { top: 0; }
  .panel--bottom { top: 600px; }

  .photo {
    position: absolute; left: 0; top: 0; width: 566px; height: 450px;
    background:
      radial-gradient(ellipse 38% 48% at 58% 42%, #e6b08f 0%, #c98a63 45%, transparent 75%),
      radial-gradient(ellipse 30% 40% at 40% 45%, #8c3a1c 0%, transparent 70%),
      linear-gradient(180deg, #6f8f86 0%, #b48a62 35%, #c49a6c 75%, #a97a4e 100%);
  }

  .colour-bars { position: absolute; left: 0; top: 455px; width: 566px; height: 59px; }
  .colour-bars span { position: absolute; top: 0; height: 59px; }
  .c-mid { background: var(--blue-mid); }
  .c-deep { background: var(--blue-deep); }
  .c-bright { background: var(--blue-bright); }
  .c-light { background: var(--blue-light); }

  .footer { position: absolute; left: 0; top: 520px; width: 566px; height: 80px; background: var(--blue-light); }
  .footer__rule { position: absolute; top: 0; width: 2px; height: 20px; background: var(--white); }
  .footer__web {
    position: absolute; left: 352px; top: 9px;
    font: 700 10.5px/1 "Arimo", sans-serif; color: var(--white);
  }
  .footer__address {
    position: absolute; left: 38px; top: 56px; white-space: nowrap;
    font: 700 9.6px/1 "Arimo", sans-serif; color: var(--blue-deep); letter-spacing: 0.2px;
  }
  .footer__address .gap { display: inline-block; width: 14px; }
  .footer__address .label { color: var(--white); font-weight: 700; }

  .copy { position: absolute; left: 606px; top: 44px; width: 224px; }
  .copy__heading {
    font: 700 25.5px/33.5px "Montserrat", sans-serif; color: var(--navy);
    letter-spacing: 1.2px; text-transform: uppercase;
  }
  .copy__lead {
    margin-top: 22px;
    font: 700 13.4px/20.8px "Arimo", sans-serif; color: var(--orange);
  }
  .copy__body {
    margin-top: 9px;
    font: 400 14.2px/20.8px "Tinos", serif; color: var(--body-grey);
    text-align: justify; text-align-last: left;
  }

  .school-name {
    position: absolute; left: 606px; width: 224px; text-align: center;
    font: 700 15px/1.25 "Montserrat", sans-serif; color: var(--navy);
    display: flex; flex-direction: column; align-items: center; gap: 8px;
  }
  .panel--top .school-name { top: 470px; }
  .panel--bottom .school-name { top: 470px; }
  .school-name__dot { width: 26px; height: 26px; border-radius: 50%; background: var(--orange); }
</style>
</head>
<body>
<main class="poster">

  <section class="panel panel--top">
    <div class="photo" role="img" aria-label="Photograph of a smiling young student with red pigtails looking upward in a classroom"></div>
    <div class="colour-bars" aria-hidden="true">
      <span class="c-mid" style="left:0;width:38px"></span>
      <span class="c-deep" style="left:38px;width:24px"></span>
      <span class="c-mid" style="left:62px;width:28px"></span>
      <span class="c-bright" style="left:96px;width:62px"></span>
      <span class="c-light" style="left:182px;width:47px"></span>
      <span class="c-deep" style="left:229px;width:9px"></span>
      <span class="c-bright" style="left:238px;width:149px"></span>
      <span class="c-mid" style="left:410px;width:35px"></span>
      <span class="c-deep" style="left:445px;width:49px"></span>
      <span class="c-mid" style="left:500px;width:66px"></span>
    </div>
    <div class="footer">
      <span class="footer__rule" style="left:330px"></span>
      <span class="footer__rule" style="left:515px"></span>
      <p class="footer__web">www.yourwebsitehere.com</p>
      <p class="footer__address">5432 ANY STREET WEST, TOWNSVILLE, ST 54321<span class="gap"></span>555.543.5432 <span class="label">tel</span><span class="gap"></span>555.543.5432 <span class="label">fax</span></p>
    </div>
    <div class="copy">
      <h1 class="copy__heading">Education<br>is the<br>foundation</h1>
      <p class="copy__lead">Teachers use an integrated approach to curriculum delivery to ensure learning is meaningful to the child.</p>
      <p class="copy__body">Lorem ipsum dolor sit amet, a erat consectetuer badipiscing elit, a sed diam nonummy dol nibh a euismod tincidunt ut laoreet a dolore magna aliquam erat volutpat. Ut te wisi enimi ad minim veniam, quis a nos trud ullamper dolore sit amet erat tis consecteur dolore sit amet.</p>
    </div>
    <div class="school-name">
      <span class="school-name__dot" aria-hidden="true"></span>
      <span>Marlowe Catholic Central<br>Elementary School</span>
    </div>
  </section>

  <section class="panel panel--bottom">
    <div class="photo" role="img" aria-label="Photograph of a smiling young student with red pigtails looking upward in a classroom"></div>
    <div class="colour-bars" aria-hidden="true">
      <span class="c-mid" style="left:0;width:38px"></span>
      <span class="c-deep" style="left:38px;width:24px"></span>
      <span class="c-mid" style="left:62px;width:28px"></span>
      <span class="c-bright" style="left:96px;width:62px"></span>
      <span class="c-light" style="left:182px;width:47px"></span>
      <span class="c-deep" style="left:229px;width:9px"></span>
      <span class="c-bright" style="left:238px;width:149px"></span>
      <span class="c-mid" style="left:410px;width:35px"></span>
      <span class="c-deep" style="left:445px;width:49px"></span>
      <span class="c-mid" style="left:500px;width:66px"></span>
    </div>
    <div class="footer">
      <span class="footer__rule" style="left:330px"></span>
      <span class="footer__rule" style="left:515px"></span>
      <p class="footer__web">www.yourwebsitehere.com</p>
      <p class="footer__address">5432 ANY STREET WEST, TOWNSVILLE, ST 54321<span class="gap"></span>555.543.5432 <span class="label">tel</span><span class="gap"></span>555.543.5432 <span class="label">fax</span></p>
    </div>
    <div class="copy">
      <h2 class="copy__heading">Education<br>is the<br>foundation</h2>
      <p class="copy__lead">Teachers use an integrated approach to curriculum delivery to ensure learning is meaningful to the child.</p>
      <p class="copy__body">Lorem ipsum dolor sit amet, a erat consectetuer badipiscing elit, a sed diam nonummy dol nibh a euismod tincidunt ut laoreet a dolore magna aliquam erat volutpat. Ut te wisi enimi ad minim veniam, quis a nos trud ullamper dolore sit amet erat tis consecteur dolore sit amet.</p>
    </div>
    <div class="school-name">
      <span class="school-name__dot" aria-hidden="true"></span>
      <span>Marlowe Catholic Central</span>
    </div>
  </section>

</main>
</body>
</html>
```